Corvane Supplies Business Card

Professional business card that stand out to our potential customers. Front and back with clean modern design

Industry/Entity Type

Oil and gas

Contact Information for Business Card

Name, address, website , office phone and cell number

Requirements
Must have
• Editable files for each employee

```html
<!DOCTYPE html>
<html lang="en">
<head>
<meta charset="utf-8">
<title>Corvane Supplies Business Card</title>
<link href="https://fonts.googleapis.com/css2?family=Roboto:wght@400;500;700&display=swap" rel="stylesheet">
<style>
  :root {
    --backdrop: #2a2a2b;
    --card-white: #f7f7f6;
    --brand-red: #e0232e;
    --brand-blue: #1ea7cf;
    --gradient-mid: #8a4a63;
    --ink: #3a3a3c;
    --ink-soft: #4e4e50;
    --on-dark: #ffffff;
  }
  * { box-sizing: border-box; margin: 0; padding: 0; }
  html, body {
    width: 1200px; height: 852px; overflow: hidden;
    background: var(--backdrop);
    font-family: "Roboto", Arial, sans-serif;
  }
  .stage {
    width: 1200px; height: 852px;
    display: flex; align-items: center; justify-content: center; gap: 48px;
  }
  .card {
    position: relative;
    width: 525px; height: 300px;
    border-radius: 26px;
    overflow: hidden;
  }
  /* Front */
  .card-front {
    background: linear-gradient(45deg, var(--brand-blue) 0%, var(--gradient-mid) 50%, var(--brand-red) 100%);
    display: flex; align-items: center; justify-content: center;
  }
  .front-wordmark {
    display: flex; align-items: center; gap: 12px;
    color: var(--on-dark);
    font-weight: 700; font-size: 30px; letter-spacing: 2px;
    text-transform: uppercase;
  }
  .mark-square {
    width: 22px; height: 22px; background: var(--on-dark);
  }
  /* Back */
  .card-back {
    background: var(--card-white);
  }
  .back-wordmark {
    position: absolute; left: 34px; top: 112px;
    display: flex; align-items: center; gap: 10px;
    color: var(--brand-red);
    font-weight: 700; font-size: 24px;
  }
  .back-wordmark .mark-square { background: var(--brand-red); width: 18px; height: 18px; }
  .contact {
    position: absolute; left: 262px; top: 58px;
    color: var(--ink);
  }
  .contact-name {
    color: var(--brand-blue);
    font-weight: 700; font-size: 20px;
  }
  .contact-title {
    font-size: 12.5px; color: var(--ink-soft); margin: 3px 0 0 10px;
  }
  .contact-address {
    font-size: 12.5px; line-height: 17px; margin: 22px 0 12px 10px;
  }
  .contact-lines { list-style: none; margin-left: 10px; }
  .contact-lines li {
    display: flex; align-items: center; gap: 8px;
    font-size: 12.5px; line-height: 18px;
  }
  .contact-lines svg { width: 11px; height: 11px; fill: var(--brand-red); flex: none; }
  .edge-band {
    position: absolute; left: 0; right: 0; bottom: 0; height: 8px;
    display: flex;
  }
  .edge-band .band-red { flex: 0 0 58%; background: var(--brand-red); }
  .edge-band .band-blue { flex: 1; background: var(--brand-blue); }
</style>
</head>
<body>
<main class="stage">
  <section class="card card-front" aria-label="Card front">
    <div class="front-wordmark"><span class="mark-square"></span>Corvane Supplies</div>
  </section>

  <section class="card card-back" aria-label="Card back">
    <div class="back-wordmark"><span class="mark-square"></span>Corvane Supplies</div>
    <div class="contact">
      <h1 class="contact-name">Dana Reyes Hill</h1>
      <p class="contact-title">Managing Director</p>
      <p class="contact-address">412 Larkin Ave Suite 3<br>Brenton, Tx 79214</p>
      <ul class="contact-lines">
        <li>
          <svg viewBox="0 0 24 24" aria-hidden="true"><path d="M6.6 10.8a15 15 0 0 0 6.6 6.6l2.2-2.2a1 1 0 0 1 1-.25 11.4 11.4 0 0 0 3.6.57 1 1 0 0 1 1 1V20a1 1 0 0 1-1 1A17 17 0 0 1 3 4a1 1 0 0 1 1-1h3.5a1 1 0 0 1 1 1c0 1.25.2 2.45.57 3.6a1 1 0 0 1-.25 1z"/></svg>
          (555)014-2270
        </li>
        <li>
          <svg viewBox="0 0 24 24" aria-hidden="true"><path d="M2 5h20v14H2z M2 5l10 8 10-8" stroke="#f7f7f6" stroke-width="1.5"/></svg>
          sales@corvanesupplies.com
        </li>
        <li>
          <svg viewBox="0 0 24 24" aria-hidden="true"><circle cx="12" cy="12" r="10"/><path d="M2 12h20M12 2c3 3 3 17 0 20M12 2c-3 3-3 17 0 20" stroke="#f7f7f6" stroke-width="1.5" fill="none"/></svg>
          www.corvanesupplies.com
        </li>
      </ul>
    </div>
    <div class="edge-band"><span class="band-red"></span><span class="band-blue"></span></div>
  </section>
</main>
</body>
</html>
```